Nine Lanterns Quill House Book Cover for: "Growing Older Wisely"

We are a publishing company who plans to launch the book, Growing Older Wisely, A Handy Compact Manual for Legal, Financial and Emotional Health in late 2018. We desire a book cover that creates interest, looks professional and can draw readers to open and purchase this book. Growing Older Wisely is an invaluable, self-help book which provides Generation X, Baby Boomers and their families with the following information: steps to obtain valid, reliable wills and trusts, identify and pay for health care, address end of life care and manage grief. (Please see the attached book description for more information about the book contents). The cover needs to have a "wellness", health and healing emphasis but it should not be morbid. Instead, the cover should have an uplifting, inviting and engaging feeling.

The designer should use Photoshop to develop the 5 x 7 cover. Please design the front, back cover and spine using the attached suggested layout as a guide. Use colors that complement the background colors in the author's photo and the logo for the front and back colors. Feel free to change the colors of the black rectangles on the front of the book. We are looking for a design to be added using the suggested layouts but we are open to modifications of the layout provided that all the content in the attachments are used. Below are the specifications needed for the cover:

-Use Photoshop
-Develop a front and back cover for a 5 x 7 format book
-Include the book title, subtitle and author name on the front cover as noted on the front cover attachment
-Include a book title and author names on the spine of the cover
-Use full bleed background if appropriate
-Color correct and resize images as necessary
-Insert logo and publisher’s imprint on spine and back cover as noted in attachments

For designers who are successful with this contest, we will primarily consider you for future projects.

Thanks!

Target Market(s)

Generation X, Baby Boomers and their families

Industry/Entity Type

Book Publisher

Font styles to use
Sans Serif

Colors

Designer to choose colors to be used in the design.

Requirements
Must have
• The designer should use Photoshop to develop the 5 x 7 cover. Please design the front, back cover and spine using the attached suggested layout as a guide. Use colors that complement the background colors in the author's photo and the logo for the front and back colors. Feel free to change the colors of the black rectangles on the front of the book. We are looking for a design to be added using the suggested layouts but we are open to modifications of the layout provided that all the content in the attachments are used. Below are the specifications needed for the cover:
• -Use Photoshop
• -Develop a front and back cover for a 5 x 7 format book
• -Include the book title, subtitle and author name on the front cover as noted on the front cover attachment
• -Include a book title and author names on the spine of the cover
• -Use full bleed background if appropriate
• -Color correct and resize images as necessary
• -Insert logo and publisher’s imprint on spine and back cover as noted in attachments
Nice to have
• N/A
Should not have
• The design should not specifically duplicate the layout samples or include pictures of persons on the cover. We have provided those as a guide; we are looking for innovation and professionalism.

```html
<!DOCTYPE html>
<html lang="en">
<head>
<meta charset="utf-8">
<title>Growing Older Wisely – Cover</title>
<link href="https://fonts.googleapis.com/css2?family=Crimson+Pro:ital,wght@0,400;0,500;0,600;0,700;1,400&display=swap" rel="stylesheet">
<style>
  :root {
    --plum-deep: #5a2d6f;
    --plum-text: #6b4282;
    --plum-mid: #8a62a2;
    --lavender-band: #b9a3cb;
    --lavender-light: #ebe2f2;
    --paper: #ffffff;
    --serif: "Crimson Pro", Georgia, serif;
  }
  html, body { margin: 0; padding: 0; overflow: hidden; }
  body { width: 1200px; height: 818px; background: var(--plum-mid); font-family: var(--serif); }
  .cover { position: relative; width: 1200px; height: 818px; overflow: hidden; background: var(--plum-mid); }

  .scenery {
    position: absolute; left: 0; top: 0; width: 1200px; height: 670px;
    background: linear-gradient(180deg, #8c64a4 0%, #9a74b0 40%, #7a5292 58%, #9c7cb3 66%, #5e3c74 82%, #6f4c86 100%);
  }
  .bottom-band {
    position: absolute; left: 0; top: 670px; width: 1200px; height: 148px;
    background: var(--lavender-band); border-top: 3px solid var(--plum-deep);
  }
  .author-photo {
    position: absolute; left: 0; top: 398px; width: 290px; height: 420px;
    background: radial-gradient(ellipse at 45% 40%, #a47fb9 0%, #8a62a2 45%, #6c4784 80%);
    border-radius: 140px 140px 0 0;
  }

  .bio { position: absolute; left: 48px; top: 30px; width: 232px; color: var(--paper); }
  .bio h2 { margin: 0 0 6px; font-size: 23px; font-weight: 600; text-align: center; letter-spacing: .3px; }
  .bio p { margin: 0; font-size: 15px; line-height: 19.2px; font-weight: 600; text-align: justify; }
  .bio .url { margin-top: 26px; text-align: center; font-size: 16px; font-weight: 600; }

  .blurb-panel { position: absolute; left: 290px; top: 0; width: 285px; height: 670px; background: var(--paper); }
  .blurb { position: absolute; left: 25px; top: 33px; width: 230px; color: var(--plum-text); }
  .blurb h2 { margin: 0; font-size: 22px; font-weight: 600; color: var(--plum-deep); line-height: 1; white-space: nowrap; }
  .blurb h3 { margin: 3px 0 0; font-size: 14.6px; font-weight: 600; color: var(--plum-deep); line-height: 1; }
  .blurb .tag { margin: 1px 0 8px; font-size: 11px; font-weight: 600; color: var(--plum-deep); }
  .blurb p { margin: 0; font-size: 13.6px; line-height: 18.4px; text-align: justify; }
  .imprint { position: absolute; left: 25px; top: 558px; color: var(--plum-text); font-size: 12px; line-height: 15px; }
  .imprint .press { text-transform: uppercase; }
  .publisher-mark { position: absolute; left: 25px; top: 612px; display: flex; align-items: center; gap: 8px; }
  .publisher-mark .square { width: 24px; height: 24px; background: var(--plum-deep); }
  .publisher-mark span { font-size: 13px; font-weight: 600; color: var(--plum-deep); }
  .isbn { position: absolute; left: 315px; top: 680px; font-size: 10.5px; line-height: 13.5px; color: var(--plum-deep); }

  .spine-title { position: absolute; left: 600px; top: 36px; writing-mode: vertical-rl; color: var(--lavender-light); line-height: 1.15; }
  .spine-title .main { font-size: 18px; font-weight: 500; letter-spacing: .5px; }
  .spine-title .sub { font-size: 13px; }
  .spine-authors { position: absolute; left: 575px; top: 712px; width: 58px; text-align: center; font-size: 7px; line-height: 8px; color: var(--plum-deep); font-weight: 600; }
  .spine-mark { position: absolute; left: 575px; top: 751px; width: 58px; text-align: center; font-size: 5.5px; color: var(--plum-deep); }

  .front { position: absolute; left: 660px; top: 0; width: 530px; text-align: center; color: var(--lavender-light); }
  .quote { margin-top: 28px; font-size: 24px; color: #f4eef8; }
  .quote em { font-style: italic; }
  .title-top { margin-top: 10px; font-size: 106px; font-weight: 600; line-height: .95; letter-spacing: 1px; }
  .title-bottom { margin-top: 4px; font-size: 64px; font-weight: 600; line-height: 1; letter-spacing: 1px; }
  .subtitle-caps { margin-top: 16px; font-size: 26px; font-weight: 600; line-height: 1; color: #f6f0fa; }
  .subtitle { font-size: 27px; font-weight: 600; line-height: 1.2; color: #f6f0fa; white-space: nowrap; }
  .authors { position: absolute; left: 660px; top: 688px; width: 530px; text-align: center; color: var(--plum-deep); font-size: 42px; font-weight: 600; line-height: 50px; white-space: nowrap; }
  .authors .amp { font-size: 30px; }
</style>
</head>
<body>
<div class="cover">
  <div class="scenery" role="img" aria-label="Purple-toned mountain lake landscape at dusk with reflections, pine trees and reeds"></div>
  <div class="bottom-band"></div>
  <div class="author-photo" role="img" aria-label="Portrait photograph of the author in a dark blazer"></div>

  <section class="bio">
    <h2>RENATA L. ASHBY</h2>
    <p>Renata L. Ashby holds an advanced degree in Public Administration from Eastbrook State University and is currently an Administrator at the Westland Department of Community Services. Collaborator Martin J. Okafor is an attorney who has practiced for thirty-five years in the areas of family law, wills, trusts, and estate planning. In Growing Older Wisely, the two have pooled their expertise to provide an invaluable guide to all the issues involved in caring for a loved one at the end of his or her life.</p>
    <div class="url">www.renataashbywrites.com</div>
  </section>

  <div class="blurb-panel">
    <section class="blurb">
      <h2>GROWING OLDER WISELY</h2>
      <h3>A HANDY COMPACT MANUAL</h3>
      <div class="tag">for Legal, Financial and Emotional Health</div>
      <p>Death and taxes may be inevitable, but they both require a lot of preparation. Fifty percent of America’s seventy-four million baby boomers have parents eighty or older, and nearly half of those boomers haven’t discussed end-of-life issues with their loved ones.</p>
      <p>In Growing Older Wisely, the authors present a detailed, step-by-step guide on how to deal with aging. They tackle issues such as wills and trusts, estate planning, senior housing, caregiving, hospice care, and death and bereavement. Their approach is lighthearted but thorough, and they provide a sorely needed examination of all the details involved in growing old in America.</p>
      <p>Renata L. Ashby is a social services administrator, and Contributor Martin J. Okafor is an attorney. They have combined their skills and knowledge to give readers a practical understanding of the issues involved in caring for an elderly family member.</p>
    </section>
    <div class="imprint">
      <div class="press">Nine Lanterns Quill House</div>
      <div>An Imprint of Nine Lanterns Quill</div>
    </div>
    <div class="publisher-mark"><div class="square"></div><span>Nine Lanterns Quill</span></div>
  </div>
  <div class="isbn">ISBN: 978-1-000-11842-6 (paperback)<br>ISBN: 978-1-000-11843-3 (ebook)</div>

  <div class="spine-title">
    <div class="main">GROWING OLDER WISELY</div>
    <div class="sub">A Handy Compact Manual for Legal, Financial and Emotional Health</div>
  </div>
  <div class="spine-authors">ASHBY<br>with<br>OKAFOR</div>
  <div class="spine-mark">Nine Lanterns</div>

  <header class="front">
    <div class="quote">“Indispensable!” – <em>The Lanternfield Gazette</em></div>
    <div class="title-top">GROWING</div>
    <div class="title-bottom">OLDER WISELY</div>
    <div class="subtitle-caps">A HANDY COMPACT MANUAL</div>
    <div class="subtitle">for Legal, Financial and Emotional Health</div>
  </header>
  <div class="authors">RENATA L. ASHBY, M.P.A. <span class="amp">&amp;</span><br>MARTIN J. OKAFOR, ESQ.</div>
</div>
</body>
</html>
```